Brightmoor Co Trade Show Flyer

We need a brochure design (8.5 x 11) Info in the design (refer to rough draft I drew on Paper): "#1 selling tool to aquire new franchisees has been video testimonials" - Martin L. Greaves, C.E.O Kolva Smoothie Franchise Testimonials - Let your franchisees do the selling for you. Franchisee testimonial: $10,000 / per Franchisee Includes: • 2 minute Video • 1 minute add for your franchise's location • Concept creation • Communication with franchisee • Travel to their location • All rental equipment • 1 round of corrections • Animated logo • Licensed music ******* For 25% Discount section (next to middle box), please put the "Venture Fairground Logo" Great to use on all your social media (USE logos and icons) • Website • Clips • Link • Page • Snap • Chirp • Phone calls • Emails • In person meetings Some of our clients: (use the logos I uploaded - in round boxes as in draft) LOGO (Brightmoor Franchise Testimonial) www.brightmoorstories.example (866) 555-0187

Target Market(s)

Franchise owners

Colors

Designer to choose colors to be used in the design.

Requirements

```html
<!DOCTYPE html>
<html lang="en">
<head>
<meta charset="utf-8">
<title>Brightmoor Co Trade Show Flyer</title>
<link rel="stylesheet" href="https://fonts.googleapis.com/css2?family=Noticia+Text:wght@400;700&family=Source+Sans+3:wght@400;600;700&display=swap">
<style>
  :root {
    --teal: #1aa99a;
    --teal-bright: #22b3a3;
    --band-start: #1b9fb3;
    --band-end: #0d64b3;
    --ink: #333333;
    --white: #ffffff;
    --page-bg: #e9e9e9;
    --icon-line: #1aa99a;
    --cloud: rgba(255,255,255,0.28);
  }
  * { box-sizing: border-box; margin: 0; padding: 0; }
  html, body { width: 1033px; height: 1200px; overflow: hidden; background: var(--page-bg); }
  .flyer {
    position: absolute; left: 74px; top: 30px; width: 884px; height: 1140px;
    background: var(--white); overflow: hidden;
    font-family: "Source Sans 3", Arial, sans-serif; color: var(--ink);
  }
  .top-rule { position: absolute; top: 32px; height: 10px; background: var(--teal); }
  .top-rule.left { left: 0; width: 345px; }
  .top-rule.right { right: 0; width: 345px; }
  .brand {
    position: absolute; left: 355px; top: 8px; width: 174px; text-align: center;
    font-family: "Noticia Text", Georgia, serif; font-weight: 700; color: #111;
  }
  .brand-mark { width: 30px; height: 30px; border-radius: 50%; background: #111; margin: 0 auto 4px; }
  .brand-name { font-size: 21px; letter-spacing: 1px; line-height: 1; }
  .brand-sub { font-size: 8px; letter-spacing: 0.5px; margin-top: 3px; }
  .title {
    position: absolute; left: 36px; top: 92px;
    font-family: "Noticia Text", Georgia, serif; font-weight: 400;
    font-size: 64px; line-height: 70px; color: #333;
  }
  .quote {
    position: absolute; left: 36px; top: 252px; width: 420px;
    font-family: "Noticia Text", Georgia, serif; font-size: 19px; line-height: 22px; color: var(--teal);
    white-space: nowrap;
  }
  .quote-author { position: absolute; left: 36px; top: 302px; font-family: "Noticia Text", Georgia, serif; font-size: 16px; color: #444; }
  .hero-art {
    position: absolute; left: 462px; top: 100px; width: 404px; height: 190px; border-radius: 60px;
    background: radial-gradient(circle at 30% 50%, #f39a3a 0%, transparent 40%),
                radial-gradient(circle at 55% 40%, #d71f5d 0%, transparent 40%),
                radial-gradient(circle at 80% 55%, #2b8fd0 0%, transparent 42%),
                linear-gradient(90deg, #9cc94a, #e9486f, #2f9fd4);
    opacity: 0.85;
  }
  .offer-band {
    position: absolute; left: 0; top: 350px; width: 884px; height: 386px;
    background: linear-gradient(90deg, var(--band-start), var(--band-end) 70%, #1594c0);
  }
  .cloud { position: absolute; background: var(--cloud); border-radius: 40px; }
  .discount-badge { position: absolute; left: 80px; top: 28px; width: 284px; height: 330px; }
  .discount-text {
    position: absolute; left: 0; top: 78px; width: 284px; text-align: center;
    font-family: "Noticia Text", Georgia, serif; color: #333;
  }
  .discount-value { font-size: 60px; line-height: 64px; }
  .discount-label { font-size: 31px; line-height: 36px; }
  .partner-name {
    position: absolute; left: 82px; top: 210px; width: 120px;
    font-family: "Source Sans 3", Arial, sans-serif; font-weight: 700; font-size: 21px; line-height: 22px; color: var(--white);
  }
  .offer-heading {
    position: absolute; left: 442px; top: 26px; width: 420px;
    font-weight: 700; font-size: 25px; line-height: 31px; color: var(--white);
  }
  .includes { position: absolute; left: 442px; top: 112px; list-style: none; color: var(--white); font-size: 16px; }
  .includes li { height: 24.5px; display: flex; align-items: center; gap: 8px; }
  .includes svg { width: 12px; height: 12px; flex: none; }
  .usage-tab {
    position: absolute; left: 202px; top: 736px; width: 476px; height: 44px;
    background: var(--teal-bright); border-radius: 0 0 30px 30px;
    font-family: "Noticia Text", Georgia, serif; font-size: 20px; color: var(--white);
    display: flex; align-items: center; justify-content: center;
  }
  .channels { position: absolute; left: 50px; top: 806px; width: 784px; display: flex; justify-content: space-between; }
  .channel {
    width: 44px; height: 44px; border-radius: 50%; border: 1px solid #bbb; background: var(--white);
    display: flex; align-items: center; justify-content: center;
    font-weight: 700; font-size: 11px; color: var(--icon-line);
  }
  .channel svg { width: 24px; height: 24px; }
  .trusted-label { position: absolute; left: 0; top: 884px; width: 884px; text-align: center; font-family: "Noticia Text", Georgia, serif; font-size: 15px; color: #333; }
  .clients { position: absolute; left: 110px; top: 922px; width: 664px; display: flex; justify-content: space-between; }
  .client {
    width: 88px; height: 88px; border-radius: 50%; background: var(--white);
    box-shadow: 0 2px 5px rgba(0,0,0,0.35);
    display: flex; align-items: center; justify-content: center; text-align: center;
    font-weight: 700; font-size: 13px; line-height: 15px; color: #1e5aa8; padding: 8px;
  }
  .footer { position: absolute; left: 0; top: 1030px; width: 884px; height: 110px; }
  .footer-wave { position: absolute; left: 0; top: 0; }
  .footer-phone {
    position: absolute; left: 0; top: 36px; width: 884px; display: flex; justify-content: center; align-items: center; gap: 12px;
    font-size: 24px; color: var(--white);
  }
  .phone-icon { width: 26px; height: 26px; flex: none; }
  .footer-url { position: absolute; left: 0; top: 78px; width: 884px; text-align: center; font-weight: 700; font-size: 18px; color: var(--white); }
</style>
</head>
<body>
<main class="flyer">
  <div class="top-rule left"></div>
  <div class="top-rule right"></div>
  <div class="brand">
    <div class="brand-mark"></div>
    <div class="brand-name">BRIGHTMOOR</div>
    <div class="brand-sub">FRANCHISE TESTIMONIAL</div>
  </div>

  <h1 class="title">Franchise<br>Testimonials</h1>
  <p class="quote">“#1 selling tool to aquire new franchisees<br>has been video testimonials”</p>
  <p class="quote-author">- Martin L. Greaves, C.E.O</p>
  <div class="hero-art" role="img" aria-label="Cluster of colourful social media speech bubbles and icons"></div>

  <section class="offer-band">
    <div class="cloud" style="left:90px;top:14px;width:80px;height:30px"></div>
    <div class="cloud" style="left:362px;top:190px;width:64px;height:38px"></div>
    <div class="cloud" style="left:700px;top:232px;width:130px;height:54px"></div>
    <div class="cloud" style="left:22px;top:278px;width:106px;height:50px"></div>
    <div class="cloud" style="left:700px;top:330px;width:96px;height:40px"></div>

    <div class="discount-badge">
      <svg width="284" height="330" viewBox="0 0 284 330">
        <polygon points="142,0 284,82 284,248 142,330 0,248 0,82" fill="#ffffff"/>
        <polygon points="0,192 284,192 284,248 142,330 0,248" fill="#1aa99a"/>
        <rect x="70" y="196" width="144" height="86" fill="#21b09a"/>
      </svg>
      <div class="discount-text">
        <div class="discount-value">25%</div>
        <div class="discount-label">Discount for</div>
      </div>
      <div class="partner-name">Venture Fairground</div>
    </div>

    <h2 class="offer-heading">LET YOUR FRANCHISEES DO THE SELLING FOR YOU.</h2>
    <ul class="includes">
      <li><svg viewBox="0 0 12 12"><path d="M1 6 L4.5 9.5 L11 2" stroke="#7fe0c8" stroke-width="2" fill="none"/></svg>$10,000 / per testimonial</li>
      <li><svg viewBox="0 0 12 12"><path d="M1 6 L4.5 9.5 L11 2" stroke="#7fe0c8" stroke-width="2" fill="none"/></svg>2 minute Video</li>
      <li><svg viewBox="0 0 12 12"><path d="M1 6 L4.5 9.5 L11 2" stroke="#7fe0c8" stroke-width="2" fill="none"/></svg>1 minute add for your franchise's location</li>
      <li><svg viewBox="0 0 12 12"><path d="M1 6 L4.5 9.5 L11 2" stroke="#7fe0c8" stroke-width="2" fill="none"/></svg>Concept creation</li>
      <li><svg viewBox="0 0 12 12"><path d="M1 6 L4.5 9.5 L11 2" stroke="#7fe0c8" stroke-width="2" fill="none"/></svg>Communication with franchisee</li>
      <li><svg viewBox="0 0 12 12"><path d="M1 6 L4.5 9.5 L11 2" stroke="#7fe0c8" stroke-width="2" fill="none"/></svg>Travel to their location</li>
      <li><svg viewBox="0 0 12 12"><path d="M1 6 L4.5 9.5 L11 2" stroke="#7fe0c8" stroke-width="2" fill="none"/></svg>All rental equipment</li>
      <li><svg viewBox="0 0 12 12"><path d="M1 6 L4.5 9.5 L11 2" stroke="#7fe0c8" stroke-width="2" fill="none"/></svg>1 round of corrections</li>
      <li><svg viewBox="0 0 12 12"><path d="M1 6 L4.5 9.5 L11 2" stroke="#7fe0c8" stroke-width="2" fill="none"/></svg>Animated logo</li>
      <li><svg viewBox="0 0 12 12"><path d="M1 6 L4.5 9.5 L11 2" stroke="#7fe0c8" stroke-width="2" fill="none"/></svg>Licensed music</li>
    </ul>
  </section>

  <div class="usage-tab">USE YOUR TESTIMONIALS EVERYWHERE</div>

  <div class="channels">
    <div class="channel"><svg viewBox="0 0 24 24" fill="none" stroke="#1aa99a" stroke-width="1.6"><circle cx="12" cy="12" r="9"/><ellipse cx="12" cy="12" rx="4" ry="9"/><path d="M3 12h18M5 7h14M5 17h14"/></svg></div>
    <div class="channel">Clips</div>
    <div class="channel">Link</div>
    <div class="channel">Page</div>
    <div class="channel">Snap</div>
    <div class="channel">Chirp</div>
    <div class="channel"><svg viewBox="0 0 24 24" fill="none" stroke="#1aa99a" stroke-width="1.8"><path d="M6 3h3l2 5-2 1.5c1 2.5 3 4.5 5.5 5.5L16 13l5 2v3c0 1.5-1.5 3-3 3C10 21 3 14 3 6c0-1.5 1.5-3 3-3z"/></svg></div>
    <div class="channel"><svg viewBox="0 0 24 24"><path d="M3 11 L21 3 L13 21 L11 13 Z" fill="#1aa99a"/></svg></div>
    <div class="channel"><svg viewBox="0 0 24 24" fill="#1aa99a"><circle cx="12" cy="8" r="4.5"/><path d="M3 21c0-5 4-8 9-8s9 3 9 8z"/></svg></div>
  </div>

  <p class="trusted-label">TRUSTED BY:</p>
  <div class="clients">
    <div class="client">Carrow Creamery</div>
    <div class="client">Dayline Mart</div>
    <div class="client">Kolva Smoothie</div>
    <div class="client">Tidewell Cleaning</div>
    <div class="client">Gearhaven Auto</div>
  </div>

  <footer class="footer">
    <svg class="footer-wave" width="884" height="110" viewBox="0 0 884 110">
      <defs>
        <linearGradient id="footerGradient" x1="0" x2="1" y1="0" y2="0">
          <stop offset="0" stop-color="#1b9fb3"/>
          <stop offset="0.7" stop-color="#0d64b3"/>
          <stop offset="1" stop-color="#1594c0"/>
        </linearGradient>
      </defs>
      <path d="M0 0 Q442 14 884 0 L884 110 L0 110 Z" fill="#1aa99a"/>
      <path d="M0 8 Q442 22 884 8 L884 110 L0 110 Z" fill="url(#footerGradient)"/>
    </svg>
    <div class="footer-phone">
      <svg class="phone-icon" viewBox="0 0 24 24" fill="none" stroke="#ffffff" stroke-width="1.6"><circle cx="12" cy="12" r="10.5"/><path d="M8.5 6.5h2l1 3-1.2 1c.6 1.4 1.6 2.4 3 3l1-1.2 3 1v2c0 .8-.8 1.5-1.5 1.5C10.5 16.8 7 13.3 7 8c0-.8.7-1.5 1.5-1.5z"/></svg>
      <span>(866) 555-0187</span>
    </div>
    <div class="footer-url">www.brightmoorstories.example</div>
  </footer>
</main>
</body>
</html>
```